Construction Company Website Design

I need a Website Design for a Construction Company. I have attached logo and business card design files (a.i) to match styles and text for the website. I will need design for 3 pages:
1. A Home page
2. A secondary page (will be different information pages)
3. A contact page with submision form
Website to look professional and match the 'theme' across all pages, using main colours / reverse colours as per design files. Must be clear it is a construction related website without being over the top. Happy for the construction related details (whether that be images/outlines/backgrounds etc to be fairly subtle and not overbearing on the contect of the pages. It will be the content that will be most important, not the images within.

Content has not yet been fully completed but attached is a site map. Each page will need a space for the insertion of the relevant heading and associated content for that particular page. Example can be used as per attached map. If it is preferable to have content completed for this to be a more succesful project please advise and I will complete and submit.

Target Market(s)

Clients for potential construction projects. These could be a range of people. All would be very professional, well educated and put a substantial expection on the quality of website provided.

Industry/Entity Type

Construction

Number of Pages Required

3 page

Font styles to use
Serif
Sans Serif
Other font styles liked:
• fonts preferable as per design files provided unless designer beleives a different font would suit better

Requirements
Must have
• Colour scheme to match logo and business card files provided. Fonts that match as per provided files. Pages must be consistent with the theme carrying across all pages. All pages must have contact details at the bottom of the page.
• Contents of page 1 - 'Home page': multiple tab options / logo link
• Contents of page 2 - 'Secondary page': Top and side navigation / area for information and/or images.
• Contents of page - 'Contact us page': Top and side navigation / Submission form / area for logos such as linkdin, facebook etc.
Nice to have
• Would be good to have a or some generic construction related images - outlines / shadows / effects etc. These might be background images or outlines related to the relevant industry and are consistent across the pages. Could be outlines of buildings, images of men with hardhats etc etc. Good to see colour scheme as per design files used
Should not have
• No pictures of houses. Generally no photos. If any imagery of people must not show faces/details.

```html
<!DOCTYPE html>
<html lang="en">
<head>
<meta charset="utf-8">
<title>Contact Us – Norvale Constructions</title>
<link rel="stylesheet" href="https://fonts.googleapis.com/css2?family=Montserrat:ital,wght@0,400;0,500;0,600;0,700;1,400;1,500&family=Open+Sans:wght@400&display=swap">
<style>
  :root {
    --accent: #1aa3e0;
    --text-dark: #444444;
    --text-body: #333333;
    --label: #6b6b6b;
    --field-border: #cfcfcf;
    --field-bg: #ffffff;
    --panel: #f1f1f1;
    --footer: #55514f;
    --footer-bar: #3b3938;
    --white: #ffffff;
    --header-bg: rgba(88, 88, 90, 0.78);
    --social: #8a8684;
  }
  * { box-sizing: border-box; margin: 0; padding: 0; }
  html, body { width: 1200px; height: 2288px; overflow: hidden; }
  body {
    position: relative;
    background: var(--white);
    font-family: "Open Sans", Arial, sans-serif;
    color: var(--text-body);
  }

  /* Header */
  .site-header {
    position: absolute; left: 0; top: 0; width: 1200px; height: 72px;
    background: var(--header-bg);
    border-bottom: 2px solid var(--accent);
    z-index: 2;
  }
  .brand {
    position: absolute; left: 50px; top: 22px;
    font-family: "Montserrat", Arial, sans-serif; font-weight: 500;
    font-size: 21px; letter-spacing: 2px; color: var(--white);
  }
  .main-nav {
    position: absolute; right: 68px; top: 26px;
    display: flex; gap: 22px;
    font-family: "Montserrat", Arial, sans-serif; font-weight: 500;
    font-size: 15px; color: var(--white);
  }
  .main-nav .is-active { color: var(--accent); }
  .main-nav .has-sub svg { margin-left: 3px; vertical-align: 2px; }

  /* Hero */
  .hero {
    position: absolute; left: 0; top: 0; width: 1200px; height: 623px;
    background:
      radial-gradient(ellipse 320px 260px at 420px 520px, rgba(214,130,50,0.85), rgba(214,130,50,0) 70%),
      linear-gradient(100deg, #2f5f66 0%, #5a8fb3 28%, #8fc0e6 55%, #cfe3f2 75%, #6ea7d4 100%);
  }
  .hero-title {
    position: absolute; right: 70px; top: 535px;
    font-family: "Montserrat", Arial, sans-serif; font-weight: 700;
    font-size: 78px; line-height: 1; color: var(--accent);
  }

  /* Intro */
  .intro {
    position: absolute; left: 74px; top: 682px; width: 1052px;
    font-size: 19.5px; line-height: 30px; color: var(--text-body);
    text-align: justify;
  }

  /* Enquiry */
  .enquiry {
    position: absolute; left: 0; top: 870px; width: 1200px; height: 745px;
    background: var(--panel);
  }
  .enquiry-title {
    position: absolute; left: 0; top: 60px; width: 1200px; text-align: center;
    font-family: "Montserrat", Arial, sans-serif; font-weight: 600;
    font-size: 32px; color: var(--text-dark);
  }
  .enquiry-title em { font-style: normal; color: var(--accent); }
  .field { position: absolute; }
  .field label {
    display: block; height: 18px;
    font-family: "Montserrat", Arial, sans-serif; font-weight: 700;
    font-size: 10.5px; letter-spacing: 0.4px; color: var(--label);
  }
  .input {
    height: 38px; background: var(--field-bg);
    border: 1px solid var(--field-border); position: relative;
    font-family: Arial, sans-serif; font-size: 15px; color: #222;
    padding: 9px 10px;
  }
  .input svg { position: absolute; right: 14px; top: 15px; }
  .textarea { height: 108px; }
  .submit {
    position: absolute; left: 495px; top: 682px; width: 158px; height: 34px;
    background: var(--accent); border-radius: 5px; border: none;
    font-family: "Montserrat", Arial, sans-serif; font-weight: 700;
    font-size: 17px; color: var(--white); line-height: 34px; text-align: center;
  }

  /* Map */
  .location-map {
    position: absolute; left: 123px; top: 1650px; width: 929px; height: 354px;
    border: 1px solid #bfe3f4;
    background: linear-gradient(135deg, #e8e8e6 0%, #efefec 45%, #dfe9d8 100%);
  }

  /* Footer */
  .site-footer {
    position: absolute; left: 0; top: 2078px; width: 1200px; height: 168px;
    background: var(--footer); color: var(--white);
    font-family: "Montserrat", Arial, sans-serif;
  }
  .footer-brand {
    position: absolute; left: 68px; top: 30px;
    font-weight: 500; font-size: 21px; letter-spacing: 2px;
  }
  .footer-nav {
    position: absolute; left: 69px; top: 81px;
    font-size: 12.5px; font-weight: 500; display: flex; gap: 9px;
  }
  .footer-heading {
    position: absolute; top: 25px;
    font-style: italic; font-weight: 500; font-size: 15.5px;
  }
  .footer-contact {
    position: absolute; left: 673px; top: 60px;
    font-style: italic; font-size: 15.5px; line-height: 20px;
  }
  .footer-phone { position: absolute; left: 673px; top: 138px; font-style: italic; font-size: 15.5px; }
  .social { position: absolute; left: 962px; top: 57px; display: flex; gap: 8px; }
  .social span { width: 30px; height: 30px; background: var(--social); display: block; }
  .footer-bar {
    position: absolute; left: 0; top: 2246px; width: 1200px; height: 42px;
    background: var(--footer-bar); color: var(--white);
    font-family: "Montserrat", Arial, sans-serif; font-style: italic; font-size: 14px;
  }
  .footer-bar .copyright { position: absolute; left: 62px; top: 12px; }
  .footer-bar .legal { position: absolute; right: 78px; top: 12px; }
</style>
</head>
<body>

<div class="hero" role="img" aria-label="Excavator bucket dropping soil against a blue sky with city towers"></div>
<h1 class="hero-title">CONTACT US</h1>

<header class="site-header">
  <div class="brand">NORVALE CONSTRUCTIONS</div>
  <nav class="main-nav">
    <span class="is-active">HOME</span>
    <span>ABOUT US</span>
    <span class="has-sub">SERVICES<svg width="8" height="5" viewBox="0 0 8 5"><path d="M0 0 L4 5 L8 0" fill="none" stroke="#1aa3e0" stroke-width="1.4"/></svg></span>
    <span>PROJECTS</span>
    <span>CULTURE</span>
    <span>NEWS</span>
    <span>CONTACT</span>
  </nav>
</header>

<p class="intro">Lorem ipsum dolor sit amet, consectetur adipiscing elit. Duis sit amet vehicula felis. Pellentesque dui erat, fermentum non maximus sed, scelerisque quis dui. Donec vitae blandit nisi, in eleifend dui. In aliquam massa nisl, in tincidunt massa egestas eget. Maecenas dapibus mi vel leo tristique pulvinar. Curabitur a fermentum velit, at volutpat libero. Cras facilisis nibh quis dolor ultricies, et blandit ligula egestas. Nullam in tincidunt felis.</p>

<section class="enquiry">
  <h2 class="enquiry-title">Inquire about our <em>Projects</em> and <em>Services</em></h2>

  <div class="field" style="left:126px;top:160px;width:443px"><label>FIRST NAME</label><div class="input"></div></div>
  <div class="field" style="left:618px;top:160px;width:445px"><label>LAST NAME</label><div class="input"></div></div>

  <div class="field" style="left:126px;top:233px;width:198px"><label>CONTACT PREFERENCE</label><div class="input"><svg width="10" height="6" viewBox="0 0 10 6"><path d="M1 1 L5 5 L9 1" fill="none" stroke="#333" stroke-width="1.5"/></svg></div></div>
  <div class="field" style="left:371px;top:233px;width:198px"><label>PHONE</label><div class="input"></div></div>
  <div class="field" style="left:618px;top:233px;width:445px"><label>EMAIL ADDRESS</label><div class="input"></div></div>

  <div class="field" style="left:126px;top:307px;width:443px"><label>STATE</label><div class="input"><svg width="10" height="6" viewBox="0 0 10 6"><path d="M1 1 L5 5 L9 1" fill="none" stroke="#333" stroke-width="1.5"/></svg></div></div>
  <div class="field" style="left:618px;top:307px;width:445px"><label>ZIP/POSTAL CODE</label><div class="input"></div></div>

  <div class="field" style="left:126px;top:382px;width:443px"><label>COMPANY NAME</label><div class="input"></div></div>
  <div class="field" style="left:618px;top:382px;width:445px"><label>ROLE</label><div class="input"></div></div>

  <div class="field" style="left:126px;top:455px;width:937px"><label>PLEASE DESCRIBE YOUR ORGANIZATION</label><div class="input">- Select -<svg width="10" height="6" viewBox="0 0 10 6"><path d="M1 1 L5 5 L9 1" fill="none" stroke="#333" stroke-width="1.5"/></svg></div></div>

  <div class="field" style="left:126px;top:530px;width:937px"><label>PLEASE TELL US ABOUT YOUR PROJECT SITE</label><div class="input textarea"></div></div>

  <div class="submit">Submit</div>
</section>

<div class="location-map" role="img" aria-label="Street map showing the office location"></div>

<footer class="site-footer">
  <div class="footer-brand">NORVALE CONSTRUCTIONS</div>
  <nav class="footer-nav">
    <span>HOME</span><span>|</span><span>ABOUT US</span><span>|</span><span>SERVICES</span><span>|</span><span>PROJECTS</span><span>|</span><span>CULTURE</span><span>|</span><span>NEWS</span><span>|</span><span>CONTACT</span>
  </nav>
  <div class="footer-heading" style="left:673px">CONTACT</div>
  <address class="footer-contact">Norvale Constructions Pty Limited<br>14 Harlow Street<br>Ridgeview 2190</address>
  <div class="footer-phone">0400 123 987</div>
  <div class="footer-heading" style="left:961px">CONNECT WITH US</div>
  <div class="social" aria-label="Social links"><span></span><span></span><span></span><span></span></div>
</footer>
<div class="footer-bar">
  <span class="copyright">All contents ©2018 Norvale Construction Pty Limited. All rights reserved.</span>
  <span class="legal">SITE MAP &nbsp;-&nbsp; PRIVACY POLICY</span>
</div>

</body>
</html>
```